High-end construction company needs a business card design

We need a modern looking business card that draws people in, is memorable and looks so good people will want to sick it on their fridges.
On the first side what is needed are:
Logo
My name - Tomas Verbelk
Title - Managing Director
Website - www.kravel.co.uk
Email - tomas@kravel.co.uk
Telephone - 020 5194 6381
Mobile - 07845319027
On the back side was is needed is a list of all the services we provide:
-Kitchen Renovations
-Bathroom Renovations
-House Renovations
-Garage Conversions
-Extensions
-Loft Conversions
-Conservatories
-Carpentry
-Tiling
-Electrical
-Plumbing & Heating
-Bricklaying
-Landscaping
-Decorating
-Plastering
We would like the colours to be the same shades as on the logo with grey or black for the words.
Target Market(s)
Anyone who needs building work done
Contact Information for Business Card
This business card is for a construction company which strives to deliver excellent service and quality.
The look and feel of the card should represent this.
Requirements
Must have
- On the first side what is needed are:
Logo
My name - Tomas Verbelk
Title - Managing Director
Website - www.kravel.co.uk
Email - tomas@kravel.co.uk
Telephone - 020 5194 6381
Mobile - 07845319027
Nice to have
- Cool looking features

```html
<!DOCTYPE html>
<html lang="en">
<head>
<meta charset="utf-8">
<title>Kravel Construction Ltd – Business Card</title>
<link rel="stylesheet" href="https://fonts.googleapis.com/css2?family=Montserrat:wght@400;500;700;800&display=swap">
<style>
  :root {
    --bg: #161616;
    --card: #262626;
    --card-edge: #2e2e2e;
    --green: #6cc24a;
    --text: #f2f2f2;
  }
  * { margin: 0; padding: 0; box-sizing: border-box; }
  html, body { width: 1200px; height: 900px; overflow: hidden; }
  body {
    background: var(--bg);
    font-family: "Montserrat", sans-serif;
    color: var(--text);
    position: relative;
  }
  .card {
    position: absolute;
    left: 230px;
    width: 740px;
    height: 420px;
    background: radial-gradient(ellipse at 70% 40%, var(--card-edge), var(--card));
    border-bottom: 7px solid var(--green);
    overflow: hidden;
  }
  .card--back { top: 20px; }
  .card--front { top: 460px; }

  /* Back: services */
  .services {
    position: absolute;
    left: 48px;
    top: 34px;
    list-style: none;
  }
  .services li {
    font-size: 16px;
    line-height: 22.5px;
    font-weight: 500;
    padding-left: 24px;
    position: relative;
  }
  .services li::before {
    content: "";
    position: absolute;
    left: 0;
    top: 7px;
    width: 9px;
    height: 9px;
    border-radius: 50%;
    background: var(--green);
  }

  /* Brand name block */
  .brand {
    position: absolute;
    display: flex;
    align-items: center;
    gap: 14px;
    color: var(--green);
    font-weight: 800;
    text-transform: uppercase;
  }
  .brand__mark {
    width: 22px;
    height: 22px;
    background: var(--green);
    flex: none;
  }
  .brand__text { display: flex; flex-direction: column; }
  .brand__name {
    font-size: 60px;
    line-height: 1;
    letter-spacing: 1px;
  }
  .brand__sub {
    font-size: 17px;
    line-height: 1.2;
    letter-spacing: 3px;
    margin-top: 6px;
  }
  .card--back .brand { left: 420px; top: 190px; }
  .card--front .brand { left: 50px; top: 170px; }

  /* Front: contact */
  .divider {
    position: absolute;
    left: 400px;
    top: 70px;
    width: 3px;
    height: 270px;
    background: var(--green);
  }
  .contact {
    position: absolute;
    left: 440px;
    top: 70px;
  }
  .contact__name {
    color: var(--green);
    font-size: 30px;
    font-weight: 700;
  }
  .contact__title {
    font-size: 19px;
    font-weight: 500;
    margin-bottom: 18px;
  }
  .contact__address {
    font-size: 19px;
    line-height: 27px;
    font-style: normal;
    margin-bottom: 14px;
  }
  .contact__line {
    display: flex;
    align-items: center;
    gap: 10px;
    font-size: 19px;
    line-height: 29px;
  }
  .contact__line svg { width: 14px; height: 14px; flex: none; }
</style>
</head>
<body>

<section class="card card--back" aria-label="Services side">
  <ul class="services">
    <li>Kitchen Renovations</li>
    <li>Bathroom Renovations</li>
    <li>House Renovations</li>
    <li>Garage Conversions</li>
    <li>Extensions</li>
    <li>Loft Conversions</li>
    <li>Conservatories</li>
    <li>Carpentry</li>
    <li>Tiling</li>
    <li>Electrical</li>
    <li>Plumbing &amp; Heating</li>
    <li>Bricklaying</li>
    <li>Landscaping</li>
    <li>Decorating</li>
    <li>Plastering</li>
  </ul>
  <div class="brand">
    <span class="brand__mark"></span>
    <span class="brand__text">
      <span class="brand__name">Kravel</span>
      <span class="brand__sub">Construction Ltd</span>
    </span>
  </div>
</section>

<section class="card card--front" aria-label="Contact side">
  <div class="brand">
    <span class="brand__mark"></span>
    <span class="brand__text">
      <span class="brand__name">Kravel</span>
      <span class="brand__sub">Construction Ltd</span>
    </span>
  </div>
  <div class="divider"></div>
  <div class="contact">
    <h1 class="contact__name">Tomas Verbelk</h1>
    <p class="contact__title">Managing Director</p>
    <address class="contact__address">14-16 Harlow Street,<br>London, N4 2PL</address>
    <p class="contact__line">
      <svg viewBox="0 0 16 16"><path d="M3 1h3l1.5 4-2 1.5a9 9 0 0 0 4 4L11 8.5l4 1.5v3a2 2 0 0 1-2 2A12 12 0 0 1 1 3a2 2 0 0 1 2-2z" fill="#6cc24a"/></svg>
      020 5194 6381
    </p>
    <p class="contact__line">
      <svg viewBox="0 0 16 16"><rect x="4" y="1" width="8" height="14" rx="1.5" fill="none" stroke="#6cc24a" stroke-width="1.6"/><circle cx="8" cy="12.3" r="0.9" fill="#6cc24a"/></svg>
      07845319027
    </p>
    <p class="contact__line">
      <svg viewBox="0 0 16 16"><rect x="1" y="3" width="14" height="10" rx="1" fill="none" stroke="#6cc24a" stroke-width="1.6"/><path d="M1.5 3.5 8 9l6.5-5.5" fill="none" stroke="#6cc24a" stroke-width="1.6"/></svg>
      tomas@kravel.co.uk
    </p>
    <p class="contact__line">
      <svg viewBox="0 0 16 16"><circle cx="8" cy="8" r="6.5" fill="none" stroke="#6cc24a" stroke-width="1.5"/><ellipse cx="8" cy="8" rx="3" ry="6.5" fill="none" stroke="#6cc24a" stroke-width="1.2"/><path d="M1.5 8h13" stroke="#6cc24a" stroke-width="1.2"/></svg>
      www.kravel.co.uk
    </p>
  </div>
</section>

</body>
</html>
```